FOLDER

I need a fine folder that will contain other items like brochures, flyers etc. This folder will be used to reach potential customers. The project will also include letter head
Updates

Please provide the following:
1. While we have the small envelop also include a big envelop that will contain the folder.
2. Please design a letterhead
3. Include in the design:
- Company name: Tarvo Cleaning & Facility Services Nigeria Limited.
- Our Logo. I have attached it.
- Moto: Setting new cleaning standards...
- Website: www.tarvo-cleaning.com.ng
- E-mail: nigeria@tarvo-cleaning.com
- Tel: 08127365904, 07069318472
Please give the size / dimensions of your designs (width and height).

Target Market(s)

households, offices etc. The business is cleaning and facility services

Requirements
Must have
• Please provide the following:
3. Include in the design:

```html
<!DOCTYPE html>
<html lang="en">
<head>
<meta charset="utf-8">
<title>Tarvo Cleaning – Letterhead Options</title>
<link rel="stylesheet" href="https://fonts.googleapis.com/css2?family=Arimo:wght@400;700&family=Open+Sans:wght@400;600&display=swap">
<style>
  :root {
    --navy: #2e3f8f;
    --blue-deep: #1a5fae;
    --blue-mid: #2a86c8;
    --blue-light: #6ab7e6;
    --blue-pale: #cfe6f6;
    --grey-bar: #d6d8db;
    --grey-text: #8a8f98;
    --ink: #1d1d1d;
    --red: #d9261c;
    --sheet-edge: #b9bcc0;
    --paper: #ffffff;
  }
  * { margin: 0; padding: 0; box-sizing: border-box; }
  html, body { width: 1200px; height: 529px; overflow: hidden; background: var(--paper); }
  body { position: relative; font-family: "Arimo", Arial, sans-serif; color: var(--ink); }

  .sheet {
    position: absolute; top: 0; width: 382px; height: 494px;
    border: 1px solid var(--sheet-edge); border-top: none; background: var(--paper); overflow: hidden;
  }
  .sheet--one { left: 0; }
  .sheet--two { left: 402px; }
  .sheet--three { left: 804px; }

  .option-label {
    position: absolute; top: 514px; width: 382px; text-align: center;
    font-family: "Arimo", Arial, sans-serif; font-size: 8px; color: var(--ink);
  }

  .brand {
    position: absolute; display: flex; align-items: center; gap: 6px;
    font-family: "Open Sans", Arial, sans-serif; font-weight: 600; color: var(--navy);
  }
  .brand__dot { width: 14px; height: 14px; border-radius: 50%; background: var(--navy); }
  .brand__name { font-size: 17px; letter-spacing: 0.5px; }

  .sheet--one .brand { left: 24px; top: 26px; }
  .sheet--two .brand { left: 24px; top: 25px; }

  .contact-stack {
    position: absolute; right: 22px; top: 18px; text-align: right;
    font-weight: 700; font-size: 8px; line-height: 11px;
  }
  .contact-stack .indent { display: block; }

  .sun-rays { position: absolute; right: 0; top: 0; }
  .swoosh, .deco { position: absolute; left: 0; top: 0; }

  .web-strip {
    position: absolute; left: 169px; top: 0; width: 213px; height: 26px;
  }
  .web-strip__tint { position: absolute; inset: 0 0 16px 0; display: flex; }
  .web-strip__tint span { flex: 1; }
  .web-strip__tint span:nth-child(1) { background: var(--blue-pale); }
  .web-strip__tint span:nth-child(2) { background: #b9dcf3; }
  .web-strip__tint span:nth-child(3) { background: #d9ecf8; }
  .web-strip__bar {
    position: absolute; left: 0; right: 0; top: 10px; height: 16px;
    background: var(--grey-bar); border-bottom-left-radius: 8px;
    font-weight: 700; font-size: 8px; letter-spacing: 3.4px; color: #4a4d52;
    padding-left: 14px; line-height: 16px;
  }

  .contact-line {
    position: absolute; font-size: 7px;
  }
  .sheet--two .contact-line { left: 86px; top: 463px; color: #555a60; font-family: "Open Sans", Arial, sans-serif; }
  .sheet--two .contact-line span + span { margin-left: 8px; }

  .footer-bands { position: absolute; left: 0; right: 0; bottom: 0; height: 6px; display: flex; }
  .footer-bands span { flex: 1; }
  .footer-bands span:nth-child(1) { background: var(--blue-light); }
  .footer-bands span:nth-child(2) { background: var(--blue-mid); }
  .footer-bands span:nth-child(3) { background: var(--blue-deep); }

  .web-tab {
    position: absolute; left: 0; top: 0; width: 126px; height: 10px;
    background: var(--red); clip-path: polygon(0 0, 100% 0, 92% 100%, 0 100%);
    color: #fff; font-weight: 700; font-size: 7px; line-height: 10px; padding-left: 10px;
  }
  .red-rule { position: absolute; left: 0; top: 463px; width: 58px; height: 8px; background: var(--red); }
  .sheet--three .contact-line { left: 62px; top: 463px; font-weight: 700; font-size: 8px; }
  .sheet--three .contact-line span + span { margin-left: 8px; }
</style>
</head>
<body>

  <!-- Option 01 -->
  <section class="sheet sheet--one">
    <svg class="sun-rays" width="90" height="80" viewBox="0 0 90 80" aria-hidden="true">
      <defs>
        <radialGradient id="rayFade" cx="90" cy="0" r="90" gradientUnits="userSpaceOnUse">
          <stop offset="0" stop-color="#e4e6e9"/>
          <stop offset="1" stop-color="#ffffff" stop-opacity="0"/>
        </radialGradient>
      </defs>
      <polygon points="90,0 30,0 90,40" fill="url(#rayFade)"/>
      <polygon points="90,0 55,80 90,80" fill="url(#rayFade)"/>
      <polygon points="90,0 5,30 20,55" fill="url(#rayFade)" opacity="0.6"/>
    </svg>

    <div class="brand"><span class="brand__dot"></span><span class="brand__name">Tarvo Cleaning</span></div>

    <div class="contact-stack">
      <span class="indent">E-mail: nigeria@tarvo-cleaning.com</span>
      <span class="indent">Tel: 08127365904</span>
      <span class="indent">07069318472</span>
    </div>

    <svg class="swoosh" width="382" height="494" viewBox="0 0 382 494" aria-hidden="true">
      <defs>
        <linearGradient id="swooshFill" x1="0" y1="0" x2="1" y2="0">
          <stop offset="0" stop-color="#2a8fd0"/>
          <stop offset="0.6" stop-color="#2557a8"/>
          <stop offset="1" stop-color="#2e2f8a"/>
        </linearGradient>
        <path id="swooshLine" d="M22,462 Q170,500 320,470"/>
      </defs>
      <path d="M0,446 Q200,480 380,437 Q260,492 60,494 L0,494 Z" fill="url(#swooshFill)"/>
      <text font-family="Arimo, Arial, sans-serif" font-weight="700" font-size="8" letter-spacing="4.2" fill="#ffffff">
        <textPath href="#swooshLine">www.tarvo-cleaning.com.ng</textPath>
      </text>
    </svg>
  </section>
  <p class="option-label" style="left:0">Option 01</p>

  <!-- Option 02 -->
  <section class="sheet sheet--two">
    <div class="brand"><span class="brand__dot"></span><span class="brand__name">Tarvo Cleaning</span></div>

    <div class="web-strip">
      <div class="web-strip__tint"><span></span><span></span><span></span></div>
      <div class="web-strip__bar">www.tarvo-cleaning.com.ng</div>
    </div>

    <svg class="deco" width="382" height="494" viewBox="0 0 382 494" aria-hidden="true">
      <circle cx="363" cy="110" r="12" fill="#aab0d6"/>
      <text transform="translate(380 480) rotate(-90)" font-family="Open Sans, Arial, sans-serif" font-weight="400" font-size="34" letter-spacing="3" fill="var(--grey-text)">TARVO CLEANING</text>
    </svg>

    <p class="contact-line"><span>E-mail: nigeria@tarvo-cleaning.com</span><span>Tel: 08127365904 - 07069318472</span></p>

    <div class="footer-bands"><span></span><span></span><span></span></div>
  </section>
  <p class="option-label" style="left:402px">Option 02</p>

  <!-- Option 03 -->
  <section class="sheet sheet--three">
    <div class="web-tab">www.tarvo-cleaning.com.ng</div>

    <svg class="deco" width="382" height="494" viewBox="0 0 382 494" aria-hidden="true">
      <circle cx="365" cy="222" r="10" fill="var(--red)"/>
      <text transform="translate(377 490) rotate(-90)" font-family="Open Sans, Arial, sans-serif" font-weight="400" font-size="22" letter-spacing="2" fill="var(--navy)">TARVO CLEANING</text>
    </svg>

    <div class="red-rule"></div>
    <p class="contact-line"><span>E-mail: nigeria@tarvo-cleaning.com</span><span>Tel: 08127365904, 07069318472</span></p>
  </section>
  <p class="option-label" style="left:804px">Option 03</p>

</body>
</html>
```